Floor Plan Brochure (Pricing & Services) for Real Estate Agents

We are a company that help with the marketing properties for sale. It is a combined service where we Styling/Staging Properties & we also provided wide variety of Floor Plans for Real Estate Agents.

The focus is on our services of Floor Plans. I have attached a file and this will give you an idea of the services that we are trying to sell and also attached is a PDF of how I would like the brochure to be laid out / but again up to you on best design layout?? I am not looking for a repeat of this design (hence the reason for a new design). We would like something professional that will appeal to the high end estate agents and sell the service of floor plans.

Ideally we would like it to continue on with our theme of our website www.roomsplendora.com.au

Will require format in indesign and we can convert to PDF.
Updates

Hi!

As I am new to this, I really know what I was after or tell you what was required.

I have updated the brief and tried to help you as much as possible. Please review and please don't hesitate to ask a question if I haven't explained properly.

Cheers
Bea

Target Market(s)

Real Estate Agents

Industry/Entity Type

Marketing

Requirements
Must have
• *A4 design layout and format in Indesign.

Front Page
*Must have front page that makes clients want to turn the page and instantly know what we are trying to sell. Floor Plans!
*with logo
*Want to achieve higher commission levels?

2nd Page
How floor plans will increase your commission

Follow on
upto you and layout.

*Must have lots of white space and only small proportion on green as pop colour, similar to first page on website.

*No boarders around pictures.

*Must include pricing and images of floor plans
Nice to have
• *On reflection would be nice to have Tri-fold layout. Just make it look good keep in mind that I would like the option to print as well as email to agents.
*Nice to have new header & footer or design layout.
*would be nice to sell each plan/service on an individual page and blurb and cost shown in a small proportion of white space. Maybe both site and floor plan on each page?
*would be nice to include script shown in attached PDF (the pricing & services that we offer, but can always cull wording depending on your design)

Should not have
• Please do not replicate the style/layout of what I have submitted in the PDF. I am looking for something professional to send to high end real estate agencies.

```html
<!DOCTYPE html>
<html lang="en">
<head>
<meta charset="utf-8">
<title>Tri-fold brochure option 2 set</title>
<link rel="stylesheet" href="https://fonts.googleapis.com/css2?family=Arimo:wght@400;700&display=swap">
<style>
:root{
  --stage:#6c7475;
  --paper:#ffffff;
  --olive:#6b7f2e;
  --olive-dark:#5d7428;
  --green:#8fae45;
  --green-light:#a9c05f;
  --lime-text:#93b13f;
  --ink:#4a4a4a;
  --rule:#b7c98a;
  --caption:#f3e600;
}
*{box-sizing:border-box;margin:0;padding:0}
html,body{width:1200px;height:596px;overflow:hidden}
body{background:var(--stage);font-family:"Arimo",Arial,sans-serif;position:relative;color:var(--ink)}
.set-title{position:absolute;top:12px;left:0;width:1200px;text-align:center;color:var(--caption);font-size:14px}
.page{position:absolute;top:34px;width:376px;height:524px;background:var(--paper);overflow:hidden}
.page--left{left:35px}
.page--center{left:412px}
.page--right{left:788px}
.page-label{position:absolute;top:573px;width:376px;text-align:center;color:#fff;font-size:14px}
.abs{position:absolute}

/* header */
.header-bar{position:absolute;left:0;top:29px;height:29px;background:var(--green)}
.header-num{position:absolute;font-weight:700;color:#fff;font-size:50px;line-height:1;-webkit-text-stroke:1px var(--green)}
.header-title{position:absolute;color:var(--olive);font-weight:700}
.page-title{font-size:21px;left:137px;top:31px}
.page-sub{font-size:12.5px;left:137px;top:58px}

/* footer */
.footer{position:absolute;left:0;right:0;bottom:0;height:59px}
.footer-top{position:absolute;left:0;right:0;top:0;height:12px;background:var(--olive-dark)}
.footer-mid{position:absolute;left:0;right:0;top:12px;height:19px;background:var(--olive-dark)}
.footer-url{position:absolute;left:0;top:12px;width:113px;height:19px;background:var(--green-light);color:#fff;font-size:6.5px;font-weight:700;padding:6px 0 0 10px}
.footer-base{position:absolute;left:0;right:0;top:31px;bottom:0;background:var(--green)}

/* art placeholders */
.art{position:absolute}
.art--plan{background:linear-gradient(135deg,#f1f1f1,#cfcfcf)}
.art--colour-plan{background:linear-gradient(135deg,#e8dcc4,#b9a98a)}
.art--site{background:radial-gradient(circle,#cfd0cc 30%,#5f8f3a 70%)}
.art--site-bw{background:radial-gradient(circle,#eeeeee 30%,#777 75%)}
.art--3d{background:linear-gradient(160deg,#d9c7a8,#8f7a5e)}

/* page 1 */
.service-label{position:absolute;left:0;width:120px;text-align:center;color:var(--lime-text);font-weight:700;font-size:7.5px}
.v-rule{position:absolute;width:1px;background:var(--rule)}
.reason{position:absolute;left:139px;width:215px}
.reason h3{color:var(--lime-text);font-size:8.5px;font-weight:700;line-height:1.35;margin-bottom:8px}
.reason p{font-size:6.6px;line-height:1.5;padding-left:11px}
.reason small{font-size:3.8px;color:#777}
.cta{position:absolute;left:140px;top:439px;color:var(--olive);font-weight:700;font-size:10px}

/* pages 2 and 3 */
.col{position:absolute}
.col h3{color:var(--lime-text);font-size:6.3px;font-weight:700;margin-bottom:8px}
.col p{font-size:6.2px;line-height:1.45;margin-bottom:12px;text-align:justify}
.price{color:var(--lime-text);font-size:5.6px;line-height:1.9}
.price-lg{color:var(--olive);font-size:6.8px;font-weight:700;margin:6px 0 20px}
.block{margin-bottom:0}
.extra{position:absolute;left:0;width:376px;top:81px;text-align:center;font-size:8px;font-weight:700;color:#333}
</style>
</head>
<body>

<div class="set-title">Tri-fold brochure option 2 set</div>

<!-- Page 1 -->
<section class="page page--left">
  <div class="header-bar" style="width:115px"></div>
  <div class="header-num" style="left:108px;top:23px">4</div>
  <h1 class="header-title" style="left:144px;top:28px;font-size:13.5px;line-height:1.15">Reasons floor plans can help you<br>&nbsp;as an agent to make more money</h1>

  <div class="service-label" style="top:88px">FLOOR PLANS</div>
  <div class="art art--plan" role="img" aria-label="Black and white floor plan drawing" style="left:22px;top:100px;width:78px;height:72px"></div>
  <div class="service-label" style="top:185px">COLOURED PLANS</div>
  <div class="art art--colour-plan" role="img" aria-label="Coloured floor plan drawing" style="left:22px;top:197px;width:78px;height:75px"></div>
  <div class="service-label" style="top:286px">SITE PLANS</div>
  <div class="art art--site" role="img" aria-label="Coloured site plan with garden" style="left:30px;top:296px;width:62px;height:62px"></div>
  <div class="service-label" style="top:383px">3D FLOOR PLANS</div>
  <div class="art art--3d" role="img" aria-label="3D rendered floor plan" style="left:22px;top:395px;width:78px;height:60px"></div>

  <div class="v-rule" style="left:117px;top:103px;height:339px"></div>

  <div class="reason" style="top:94px">
    <h3>1) INCREASE YOUR COMMISSION?</h3>
    <p>In a recent survey, agents who used floor plans reported a 26% higher commission levels. <small>(source: estate agents news)</small></p>
  </div>
  <div class="reason" style="top:182px">
    <h3>2) MORE PROSPECTIVE BUYERS THROUGH OPENS?</h3>
    <p>93% of buyers are more than likely to <small>inspect a property with a floor plan. (source: H.B.R Buyers survey 2008)</small></p>
  </div>
  <div class="reason" style="top:282px">
    <h3>3) REDUCE THE AMOUNT OF TIME YOUR LISTING<br>IS ON THE MARKET?</h3>
    <p>Including floor plans in your marketing campaign has proven to reduced the listing time on the market by up to 50%. <small>(source: H.B.R Buyers survey 2008)</small></p>
  </div>
  <div class="reason" style="top:376px">
    <h3>4) BOOST YOUR REFERRALS?</h3>
    <p>81% of vendors believe that professionally produced plans will help them sell their property faster. <small>(source: estate agents news)</small></p>
  </div>
  <div class="cta">HAVE WE GOT YOUR INTEREST?</div>

  <footer class="footer">
    <div class="footer-top"></div><div class="footer-mid"></div>
    <div class="footer-url">www.roomsplendora.com.au</div>
    <div class="footer-base"></div>
  </footer>
</section>
<div class="page-label" style="left:35px">inside left Page 1</div>

<!-- Page 2 -->
<section class="page page--center">
  <div class="header-bar" style="width:98px"></div>
  <div class="header-num" style="left:106px;top:23px">1</div>
  <h1 class="header-title page-title">PROPERTY</h1>
  <h2 class="header-title page-sub">7 different ways to market</h2>

  <div class="col" style="left:23px;top:96px;width:330px">
    <h3>WHAT DO WE OFFER?</h3>
    <p>We are not photographers pretending to be a drafter, we are qualified Interior Designers who happen to have a lifetime of experience within the real estate industry. We understand what is required to help market your property and are therefore able to offer you a wide variety of options to highlight each individual properties needs and also suit your agency brand.</p>
    <h3>WHICH PLAN TO CHOOSE?</h3>
    <p>Floor plans are regarded as one of the most important requirements as the online property buyer is able to view the entire property layout from this information. The floor plan will also give the buyer an approximate indication of the entire property size plus individual room sizes. But the question is, which of the following is going to help increase your commission? Well that depends on your listings and your agency branding. The choice is yours.</p>
  </div>

  <div class="col" style="left:23px;top:226px;width:222px">
    <h3>BLACK &amp; WHITE FLOOR PLAN</h3>
    <p>In most cases floor plans are still printed on paper and predominately in black and white and for good reason. Black and White plans a more "cleaner" and help with readability, most importantly, they saves you money on printing cost.</p>
    <div class="price">1 - 2 Bedroom &nbsp;&nbsp;&nbsp;&nbsp;$___<br>3 - 4 Bedroom &nbsp;&nbsp;&nbsp;&nbsp;$___<br>5 - 6 Bedroom &nbsp;&nbsp;&nbsp;&nbsp;$___</div>
    <div class="price-lg">Large Homes (600sqm +) $___</div>
    <h3>BLACK &amp; WHITE SITE PLAN</h3>
    <p>Site plans feature a home's floor plan relative to its grounds or grounds. If your going to use black and white floor plan, then we will produce a site plan to match.</p>
    <div class="price">Less than 1000 sqm $______ &nbsp;&nbsp;&nbsp;&nbsp;(when combined with a floor plan or $___)<br>1001sqm - 2000 sqm $______ &nbsp;(when combined with a floor plan or $___)<br>2001 sqm - 4000 sqm $______ (when combined with a floor plan or $___)</div>
    <div class="price-lg">Acerage / Estates ___</div>
  </div>
  <div class="v-rule" style="left:246px;top:228px;height:215px"></div>
  <div class="art art--plan" role="img" aria-label="Black and white floor plan drawing" style="left:258px;top:230px;width:95px;height:92px"></div>
  <div class="art art--site-bw" role="img" aria-label="Black and white site plan with trees" style="left:262px;top:345px;width:88px;height:85px"></div>

  <footer class="footer">
    <div class="footer-top"></div><div class="footer-mid"></div>
    <div class="footer-url">www.roomsplendora.com.au</div>
    <div class="footer-base"></div>
  </footer>
</section>
<div class="page-label" style="left:412px">inside center Page 2</div>

<!-- Page 3 -->
<section class="page page--right">
  <div class="header-bar" style="width:98px"></div>
  <div class="header-num" style="left:106px;top:23px">1</div>
  <h1 class="header-title page-title">PROPERTY</h1>
  <h2 class="header-title page-sub">7 different ways to market</h2>
  <div class="extra">For an extra $__ add some colour into your marketing campaign.</div>

  <div class="col" style="left:22px;top:96px;width:225px">
    <h3>COLOURED FLOOR PLAN</h3>
    <p>Color floor-plans show that you care about selling your client's listing; they add a premium, high value look to any listing and can be used in your brochures, email and websites.</p>
    <div class="price">1 - 2 Bedroom $___<br>3 - 4 Bedroom $___<br>5 - 6 Bedroom $___</div>
    <div class="price-lg" style="margin-bottom:42px">Large Homes (600sqm +) $___</div>
    <h3>COLOURED SITE PLAN</h3>
    <p>Site plans feature a home's floor plan relative to its gardens or grounds. Including prominent external features. These plans are perfect for showcasing large blocks, sub-division potential or multiple dwellings.</p>
    <div class="price">Less than 1000 sqm $___ (when combined with a floor plan or $___)<br>1001sqm - 2000 sqm $___ (when combined with a floor plan or $___)<br>2001 sqm - 4000 sqm $___ (when combined with a floor plan or $___)</div>
    <div class="price-lg">Acerage / Estates ___</div>
    <h3>FURNITURE LAYOUT</h3>
    <p>Want to showcase a new development or vacant property. We can also embed the floor plan on your website and allow buyers to explore the floor plan, decorate it, and get a real feel for their potential new home.</p>
    <div class="price">1 - 2 Bedroom $___<br>3 - 4 Bedroom $___<br>5 - 6 Bedroom $___</div>
    <div class="price-lg">Large Homes (600sqm +) $___</div>
  </div>
  <div class="v-rule" style="left:256px;top:103px;height:340px"></div>
  <div class="art art--colour-plan" role="img" aria-label="Coloured floor plan drawing" style="left:272px;top:105px;width:82px;height:85px"></div>
  <div class="art art--site" role="img" aria-label="Coloured site plan with gardens" style="left:277px;top:210px;width:78px;height:85px"></div>
  <div class="art art--colour-plan" role="img" aria-label="Furnished floor plan layout" style="left:275px;top:345px;width:80px;height:88px"></div>

  <footer class="footer">
    <div class="footer-top"></div><div class="footer-mid"></div>
    <div class="footer-url">www.roomsplendora.com.au</div>
    <div class="footer-base"></div>
  </footer>
</section>
<div class="page-label" style="left:788px">inside right Page 3</div>

</body>
</html>
```